International freight forwarder experienced in perishable handling needs a web design

We need a website designed that will allow us to capture more customers through the website. We would like a visually appealing design that is not so heavy on text. Our business covers the logistics and freight forwarding industries and we have offices in South America and the USA. Our main customers are importers USA, Europe, Asia and Russia and we currently work almost exclusively with perishable products such as fresh cut flowers, fresh exotics fruits, cacao, fresh fish etc. We would like to convey a fresh, modern approach to freight forwarding focusing on concepts such as - time sensitive, anytime-anywhere delivery, innovation, experience, reliability and confidence. Should include links with Plumetta and Worvanet. Our core solutions include: Core Services
*Air Freight
*Ocean Freight
*Warehousing & Distribution
Our industry solutions cover
*Flowers
*FMCG including, fruits, vegetables
*Live animals
*Automotive
*Consumer Goods
*Industrial
*Oil & Gas
*Pharma
* Event logistics
* Project logistics

Target Market(s)

Importers in Europe, USA, Asia, Middle East and Russia

Number of Pages Required

4 page

Font styles to use
Sans Serif

Colors
a1cd39
606060
000000

Requirements
Must have
• Photos of fresh cut flowers, FMCG such as cacao, fresh fish (packaged for shipping), fresh exotic fruits, pharma products (packaged for shipping), oil and gas etc. Internal customer login access
Nice to have
• Photos of cargo shipping carriers and cargo airline carriers. Features similar to those of following website http://www.brolvacargo.com/eng/main/index.jsp?FromURL=web
Should not have
• Too much text, needs to be visually pleasing

```html
<!DOCTYPE html>
<html lang="en">
<head>
<meta charset="utf-8">
<title>Vantrelo Alliance – Freight Forwarding</title>
<link rel="stylesheet" href="https://fonts.googleapis.com/css2?family=Arimo:wght@400;700&family=Open+Sans:ital,wght@0,400;0,600;1,400;1,600&display=swap">
<style>
:root{
  --green:#a1cd39;
  --green-dark:#8cb52a;
  --grey:#606060;
  --black:#000;
  --light:#f2f2f2;
  --white:#fff;
}
*{box-sizing:border-box;margin:0;padding:0}
html,body{width:763px;height:1200px;overflow:hidden}
body{position:relative;background:var(--white);font-family:"Open Sans",Arial,sans-serif;color:var(--grey)}
.abs{position:absolute}
.topbar{left:0;top:0;width:763px;height:14px;background:var(--black);color:var(--white);font-size:7px}
.topbar .item{position:absolute;top:2px;display:flex;align-items:center;gap:4px}
.search{position:absolute;left:492px;top:2px;width:76px;height:10px;background:var(--white);font-size:5.5px;color:#aaa;padding:1px 4px}
.logo{left:195px;top:22px;text-align:center}
.logo .mark{width:22px;height:22px;border-radius:50%;background:var(--green);margin:0 auto 6px}
.logo .name{font-family:Arimo,sans-serif;font-size:14px;color:#333}
.logo .sub{font-size:4px;letter-spacing:2px;color:#999}
.login{top:27px;font-size:6.5px;color:var(--white);display:flex}
.login span{padding:2px 3px}
.nav{top:51px;left:382px;display:flex;gap:10px;font-size:6.5px;color:#444}
.nav .on{color:var(--green)}
.rule{left:0;top:70px;width:763px;height:1px;background:#ddd}
.hero-art{left:160px;top:86px;width:420px;height:205px;background:linear-gradient(135deg,#eef3e4,#a9c96a 45%,#6b7a55 80%,#ddd)}
.hero-title{left:190px;top:117px;width:208px;padding:4px 7px;background:linear-gradient(90deg,var(--green) 70%,rgba(161,205,57,0));font-family:Arimo,sans-serif;font-weight:700;font-size:12.5px;line-height:15px;color:#1a1a1a}
.hero-line{left:0;top:292px;width:763px;height:2px;background:var(--green)}
.dots{left:357px;top:286px;width:50px;height:13px;background:var(--green);display:flex;justify-content:center;align-items:center;gap:4px}
.dots i{width:7px;height:7px;border:1px solid var(--white);border-radius:50%}
.dots i.on{background:var(--white)}
.service{top:309px;height:137px;background:var(--green);text-align:center;color:#222}
.service .ico{width:60px;height:60px;border-radius:50%;background:var(--black);margin:13px auto 10px;display:flex;align-items:center;justify-content:center}
.service h3{font-size:7px;font-weight:600}
.service p{font-size:5.5px;margin-top:5px;line-height:7.5px;color:#333}
.service .more{display:inline-block;margin-top:6px;font-size:5.5px;border:1px solid #333;background:var(--light);padding:0 5px}
.about-band{left:0;top:446px;width:763px;height:116px;background:var(--light)}
.about h2{font-size:9px;font-weight:600;color:#222}
.about p{font-size:6px;line-height:7.6px;margin-top:5px;width:220px}
.btn-green{display:inline-block;background:var(--green);color:#222;font-size:6px;padding:1px 5px;margin-top:7px;border:1px solid var(--green-dark)}
.video{left:426px;top:462px;width:142px;height:83px;background:linear-gradient(180deg,#6d7a8a,#3a4250 60%,#1c1f25)}
.video .bar{position:absolute;left:0;bottom:0;width:100%;height:9px;background:#111}
.section-title{font-family:Arimo,sans-serif;font-weight:700;font-size:10.5px;color:#111;text-align:center;width:763px;left:0}
.arrows{display:flex;gap:1px}
.arrows i{width:8px;height:8px;background:#111;display:block}
.arrows i+i{background:var(--green)}
.grid{left:195px;top:578px;width:373px;height:196px;display:grid;grid-template-columns:repeat(3,1fr);grid-template-rows:repeat(2,1fr);gap:1px;background:#333;border:1px solid #333}
.tile{position:relative;display:flex;align-items:center;justify-content:center}
.tile span{background:rgba(0,0,0,.85);color:var(--green);font-style:italic;font-size:7px;padding:5px 0;width:70px;text-align:center}
.service-band{left:190px;top:789px;width:382px;height:127px;background:linear-gradient(90deg,var(--green),#b7db62)}
.service-band h2{position:absolute;left:10px;top:26px;font-family:Arimo,sans-serif;font-weight:700;font-size:15px;color:#1a1a1a}
.service-band p{position:absolute;left:11px;top:48px;width:230px;font-family:Arimo,sans-serif;font-size:5.8px;line-height:7.6px;color:#333}
.service-band .btn{position:absolute;left:11px;top:91px;background:var(--black);color:var(--white);font-size:6px;padding:1px 5px}
.boxes{position:absolute;left:255px;top:20px;width:115px;height:85px;background:linear-gradient(160deg,#d8b98b,#b58a55);border-radius:3px}
.testi-band{left:0;top:916px;width:763px;height:166px;background:var(--light)}
.quote{left:255px;top:968px;width:253px;font-family:Arimo,sans-serif;font-size:6px;line-height:7.6px;color:#333;text-align:center}
.qmark{color:var(--green);font-family:Arimo,sans-serif;font-weight:700;font-size:14px}
.author{left:323px;top:1033px;font-style:italic;font-weight:600;font-size:7px;color:var(--green)}
.avatar{left:407px;top:1010px;width:50px;height:50px;border-radius:50%;border:2px solid var(--green);background:linear-gradient(180deg,#d9d9d9,#8a8a8a)}
.footer{left:0;top:1082px;width:763px;height:108px;background:#121212;color:var(--white)}
.flogo{position:absolute;left:195px;top:22px;text-align:center}
.flogo .mark{width:22px;height:22px;border-radius:50%;background:var(--white);margin:0 auto 6px}
.flogo .name{font-family:Arimo,sans-serif;font-size:14px}
.flogo .sub{font-size:4px;letter-spacing:2px;color:#aaa}
.vrule{position:absolute;left:303px;top:18px;width:1px;height:72px;background:#444}
.fcol{position:absolute;top:22px;font-size:6.5px}
.fcol h4{font-weight:400;font-size:7px;margin-bottom:9px}
.fcol li{list-style:none;font-size:5.8px;margin-bottom:7px;color:#ddd}
.fcol li::before{content:"•";margin-right:5px}
.fcol .row{display:flex;align-items:center;gap:5px;font-size:6px;margin-bottom:8px}
.signup{display:flex;margin-top:4px}
.signup span{font-size:4.5px;padding:1px 3px}
.social{display:flex;gap:3px}
.social i{width:10px;height:10px;border-radius:50%;display:block}
.bottombar{left:0;top:1190px;width:763px;height:10px;background:var(--green);font-size:4.5px;color:#333}
</style>
</head>
<body>

<div class="abs topbar">
  <div class="item" style="left:196px">
    <svg width="9" height="6" viewBox="0 0 9 6"><rect x=".5" y=".5" width="8" height="5" fill="none" stroke="#a1cd39"/><path d="M.5 .5l4 3 4-3" fill="none" stroke="#a1cd39"/></svg>
    info@vantreloalliance.com
  </div>
  <div class="item" style="left:311px">
    <svg width="6" height="7" viewBox="0 0 6 7"><path d="M1 0h1.5l.5 2-1 .7a4 4 0 0 0 1.8 1.8l.7-1 2 .5V5.5A1 1 0 0 1 5 6.5 5 5 0 0 1 0 1.5 1 1 0 0 1 1 0z" fill="#a1cd39"/></svg>
    1- 844 - 555 - 0192
  </div>
  <div class="search">Search</div>
</div>

<div class="abs logo">
  <div class="mark"></div>
  <div class="name">Vantrelo Alliance</div>
  <div class="sub">GROUP</div>
</div>

<div class="abs login" style="left:467px">
  <span style="background:#000">CustomerLogin</span><span style="background:var(--green);color:#222">Create Account</span>
</div>
<nav class="abs nav">
  <span class="on">Home</span><span>About Us</span><span>Services</span><span>Industry Solutions</span><span>Contacts</span>
</nav>
<div class="abs rule"></div>

<div class="abs hero-art" role="img" aria-label="Cargo ship, container truck, airplane over a green globe and a forklift with pallets"></div>
<div class="abs hero-title">Freight forwarding in Time sensitive,Experience, Reliability and Confidence.</div>
<div class="abs hero-line"></div>
<div class="abs dots"><i></i><i></i><i class="on"></i><i></i></div>

<div class="abs service" style="left:195px;width:121px">
  <div class="ico"><svg width="36" height="36" viewBox="0 0 24 24"><path d="M21 3.5c-.8-.8-2.2-.6-3 .2L14.5 7.2 5 4.5 3.5 6l7.5 4.5-3.8 3.8-2.7-.4L3.3 15l3.3 1.7L8.3 20l1.1-1.2-.4-2.7 3.8-3.8L17.3 19.8l1.5-1.5-2.7-9.5 3.5-3.5c.8-.8 1-2.2.2-3z" fill="#fff"/></svg></div>
  <h3>Air Freight</h3>
  <p>Lorem Ipsum is simply<br>dummy text..</p>
  <span class="more">More</span>
</div>
<div class="abs service" style="left:323px;width:117px">
  <div class="ico"><svg width="36" height="36" viewBox="0 0 24 24" fill="none" stroke="#fff" stroke-width="1.6"><path d="M8 4h8v4H8zM5 8h14l-2 7H7z"/><path d="M3 18c2 1.5 4 1.5 6 0s4-1.5 6 0 4 1.5 6 0M3 21c2 1.5 4 1.5 6 0s4-1.5 6 0 4 1.5 6 0"/></svg></div>
  <h3>Ocean Freight</h3>
  <p>Lorem Ipsum is simply<br>dummy text..</p>
  <span class="more">More</span>
</div>
<div class="abs service" style="left:450px;width:118px">
  <div class="ico"><svg width="38" height="36" viewBox="0 0 26 24" fill="#fff"><path d="M3 6h6l3 6v5H3zM5 8v4h5l-2-4z"/><rect x="14" y="3" width="2" height="15"/><rect x="17" y="6" width="7" height="5"/><rect x="17" y="12" width="7" height="5"/><rect x="14" y="17" width="10" height="1.5"/><circle cx="5.5" cy="19" r="2.2"/><circle cx="10.5" cy="19" r="2.2"/></svg></div>
  <h3>Warehousing &amp; Distribution</h3>
  <p>Lorem Ipsum is simply<br>dummy text..</p>
  <span class="more">More</span>
</div>

<div class="abs about-band"></div>
<div class="abs about" style="left:195px;top:461px">
  <h2>Logistics and freight forwarding industries.</h2>
  <p>Lorem Ipsum is simply dummy text of the printing and typesetting industry. Lorem Ipsum has been the industry's standard dummy text ever since the 1500s, when an unknown printer took a galley of type and scrambled it to make a type specimen book. It has survived not only five centuries, but also the leap into electronic typesetting, remaining essentially unchanged. It was popularised..</p>
  <span class="btn-green">Read More</span>
</div>
<div class="abs video" role="img" aria-label="Video still of cargo pallets being loaded beside an aircraft">
  <svg class="abs" style="left:62px;top:33px" width="17" height="17" viewBox="0 0 17 17"><circle cx="8.5" cy="8.5" r="7.5" fill="none" stroke="#a1cd39" stroke-width="1.5"/><path d="M6.5 5v7l6-3.5z" fill="#a1cd39"/></svg>
  <div class="bar"><svg class="abs" style="left:7px;top:2px" width="5" height="5" viewBox="0 0 5 5"><path d="M0 0v5l5-2.5z" fill="#fff"/></svg></div>
</div>

<div class="abs section-title" style="top:561px">OUR INDUSTRY SOLUTIONS</div>
<div class="abs arrows" style="left:549px;top:562px"><i></i><i></i></div>
<div class="abs grid">
  <div class="tile" role="img" aria-label="Red roses" style="background:linear-gradient(135deg,#b3121b,#5d0a0e)"><span>Flowers</span></div>
  <div class="tile" role="img" aria-label="Fresh fruits and vegetables" style="background:linear-gradient(135deg,#4f8f2a,#d9632a 60%,#5a2a55)"><span>Fruits&amp;vegetables</span></div>
  <div class="tile" role="img" aria-label="Panda" style="background:linear-gradient(135deg,#d8d8d8,#777)"><span>Live animals</span></div>
  <div class="tile" role="img" aria-label="Red sports car" style="background:linear-gradient(135deg,#2a3550,#b01c1c 55%,#1a1a1a)"><span>Automotive</span></div>
  <div class="tile" role="img" aria-label="Shelves of packaged groceries" style="background:linear-gradient(135deg,#d8442c,#e8b730 50%,#2f7bc0)"><span>Consumer Goods</span></div>
  <div class="tile" role="img" aria-label="Heavy industrial cargo being lifted" style="background:linear-gradient(135deg,#8fb4d4,#3f6f96)"><span>Project logistics</span></div>
</div>

<div class="abs service-band">
  <h2>THE BEST CUSTOMER SERVICE</h2>
  <p>Lorem Ipsum is simply dummy text of the printing and typesetting industry. Lorem Ipsum has been the industry's standard dummy text ever since the 1500s, when an unknown printer took a galley of type and scrambled it to make a type specimen book. It has survived not only five centuries, but also the leap into electronic typesetting, remaining essentially unchanged.</p>
  <span class="btn">Read More</span>
  <div class="boxes" role="img" aria-label="Stack of cardboard shipping boxes"></div>
</div>

<div class="abs testi-band"></div>
<div class="abs section-title" style="top:936px">TESTIMONIALS</div>
<div class="abs arrows" style="left:549px;top:938px"><i></i><i></i></div>
<div class="abs quote"><span class="qmark">“</span>Lorem ipsum dolor sit amet, consectetur adipiscing elit, sed do eiusmod tempor incididunt ut labore et dolore magna aliqua. Ut enim ad minim veniam, quis nostrud exercitation ullamco laboris. <span class="qmark">”</span></div>
<div class="abs author">Mr. Harlow chiropractor</div>
<div class="abs avatar" role="img" aria-label="Portrait of the client"></div>

<footer class="abs footer">
  <div class="flogo">
    <div class="mark"></div>
    <div class="name">Vantrelo Alliance</div>
    <div class="sub">GROUP</div>
  </div>
  <div class="vrule"></div>
  <div class="fcol" style="left:316px">
    <h4>Quick Navigation</h4>
    <ul><li>Home</li><li>About us</li><li>Services</li><li>Industry solutions</li></ul>
  </div>
  <div class="fcol" style="left:399px">
    <h4>Get in touch</h4>
    <div class="row"><svg width="6" height="7" viewBox="0 0 6 7"><path d="M1 0h1.5l.5 2-1 .7a4 4 0 0 0 1.8 1.8l.7-1 2 .5V5.5A1 1 0 0 1 5 6.5 5 5 0 0 1 0 1.5 1 1 0 0 1 1 0z" fill="#fff"/></svg>1- 844 - 555 - 0192</div>
    <div class="row"><svg width="9" height="6" viewBox="0 0 9 6"><rect x=".5" y=".5" width="8" height="5" fill="none" stroke="#fff"/><path d="M.5 .5l4 3 4-3" fill="none" stroke="#fff"/></svg>info@vantreloalliance.com</div>
    <div class="signup"><span style="background:#fff;color:#aaa;width:48px">Email address</span><span style="background:var(--green);color:#222">SIGN UP</span></div>
  </div>
  <div class="fcol" style="left:507px">
    <h4>Follow Us</h4>
    <div class="social" aria-label="Plumetta, Worvanet and other social links"><i style="background:#3b5ca0"></i><i style="background:#2fa7dd"></i><i style="background:#1f7bb6"></i><i style="background:#d8442c"></i></div>
  </div>
</footer>
<div class="abs bottombar">
  <span class="abs" style="left:196px;top:2px">Copyright © 2007-2015 VantreloAlliance. All rights reserved.</span>
  <span class="abs" style="left:490px;top:2px">Site Map</span>
  <span class="abs" style="left:521px;top:2px">Terms and Conditions</span>
</div>

</body>
</html>
```